Property risk and finance brokerage company needs a business card design

Tarlow Financial requires a business card design. Please integrate existing logo (refer uploaded file).
hex codes used on logo #002649 #008ED6 #444F51 #ADAFAA
font used - Cinzel
Contact information
Renata Sollisford
Director
Mobile: 0491 738 205
email: r.sollisford@tarlowfinancial.example.au
website: www.tarlowfinancial.example.au
CRN : 918354
PO Box 527
Ashbridge, Victoria, 3190
Horizontal orientation please
Finance

```html
<!DOCTYPE html>
<html lang="en">
<head>
<meta charset="utf-8">
<title>Tarlow Financial – Business Card</title>
<link href="https://fonts.googleapis.com/css2?family=Cinzel:wght@400&family=Questrial&family=Didact+Gothic&display=swap" rel="stylesheet">
<style>
  :root {
    --navy: #002649;
    --sky: #008ED6;
    --slate: #444F51;
    --stone: #ADAFAA;
    --card-blue: #0b5e9c;
    --card-blue-light: #1c7fc0;
    --card-white: #f3f3f3;
    --backdrop: #e4e6e8;
  }
  * { box-sizing: border-box; margin: 0; padding: 0; }
  html, body {
    width: 1200px;
    height: 900px;
    overflow: hidden;
    background: var(--backdrop);
  }
  .sheet {
    width: 1200px;
    height: 900px;
    display: flex;
    flex-direction: column;
    align-items: center;
    justify-content: center;
    gap: 44px;
  }
  .card {
    width: 640px;
    height: 390px;
    position: relative;
    box-shadow: 0 6px 18px rgba(0, 0, 0, 0.18);
    overflow: hidden;
  }
  /* Front */
  .card--front {
    background: radial-gradient(ellipse at 48% 40%, var(--card-blue-light) 0%, var(--card-blue) 45%, var(--navy) 130%);
    display: flex;
    align-items: center;
    justify-content: center;
  }
  .brand {
    display: flex;
    align-items: center;
    gap: 16px;
  }
  .brand__dot {
    width: 34px;
    height: 34px;
    border-radius: 50%;
    background: #ffffff;
  }
  .brand__name {
    font-family: "Cinzel", serif;
    font-weight: 400;
    font-size: 36px;
    letter-spacing: 2px;
    color: #ffffff;
    line-height: 1;
  }
  /* Back */
  .card--back {
    background: var(--card-white);
  }
  .card__mark {
    position: absolute;
    left: 18px;
    top: 62px;
    width: 200px;
    height: 200px;
  }
  .contact {
    position: absolute;
    right: 112px;
    top: 118px;
    text-align: right;
    font-family: "Questrial", "Didact Gothic", sans-serif;
    color: var(--slate);
  }
  .contact__name {
    font-family: "Didact Gothic", sans-serif;
    font-weight: 700;
    font-size: 19px;
    color: var(--slate);
    -webkit-text-stroke: 0.4px var(--slate);
  }
  .contact__role {
    font-size: 14px;
    color: var(--sky);
    margin-top: 3px;
    margin-bottom: 18px;
  }
  .contact__line {
    font-size: 13.5px;
    line-height: 22px;
  }
  .contact__label {
    color: var(--navy);
    font-weight: 700;
    -webkit-text-stroke: 0.3px var(--navy);
  }
</style>
</head>
<body>
<main class="sheet">
  <section class="card card--front" aria-label="Card front">
    <div class="brand">
      <span class="brand__dot"></span>
      <span class="brand__name">Tarlow Financial</span>
    </div>
  </section>

  <section class="card card--back" aria-label="Card back">
    <svg class="card__mark" viewBox="0 0 200 200" role="img" aria-label="Brand mark area">
      <defs>
        <linearGradient id="markFill" x1="0" y1="0" x2="1" y2="1">
          <stop offset="0" stop-color="#1e86cc"/>
          <stop offset="1" stop-color="#0b4f8a"/>
        </linearGradient>
      </defs>
      <circle cx="100" cy="100" r="90" fill="url(#markFill)"/>
    </svg>

    <div class="contact">
      <p class="contact__name">Renata Sollisford</p>
      <p class="contact__role">Managing Director</p>
      <p class="contact__line">PO Box 527</p>
      <p class="contact__line">Ashbridge, Victoria, 3190</p>
      <p class="contact__line"><span class="contact__label">Mobile:</span> 0491 738 205</p>
      <p class="contact__line"><span class="contact__label">email:</span> r.sollisford@tarlowfinancial.example.au</p>
      <p class="contact__line"><span class="contact__label">Credit Rep No. :</span> 918 354</p>
    </div>
  </section>
</main>
</body>
</html>
```